We need a web designer/programmer for Bright Harbor Ltd in London who's primary aid is to assist young people to find activities they'd like to do in their area. the MarbleTrove is mainly a post code or key word search engine. my brief attached shows what I want the web to do and how it should look. the Friends/KoruValers page is almost like a dating site. instead of choose blond hair blue eyed, young people search for friend who's doing similar activities or wearing the same size mountain boot etc so that they could share. hope it all make sense. I really want the website to go live and launch party at the end of Sept/early Oct. hope that's realistic. Thank you. Regards, Mab

Target Market(s)

young people 14-25

Number of Pages Required

5+ page

Font styles to use
Sans Serif

Requirements
Must have
• search engine, interactive, chat, user registration. remote editing with security code for my customers.
• needs to be colourful to attract young people.
• colour match the Bright Harbor Logo
Nice to have
• matching style to the KoruVal-hub.example web

```html
<!DOCTYPE html>
<html lang="en">
<head>
<meta charset="utf-8">
<title>Bright Harbor – We Nurture People</title>
<link rel="stylesheet" href="https://fonts.googleapis.com/css2?family=Arimo:wght@400;700&display=swap">
<style>
:root{
  --green:#6aa512;
  --green-dark:#4f7f0c;
  --plum:#3b1520;
  --orange:#f47b0a;
  --yellow:#f7c600;
  --ink:#222;
  --grey-text:#8a8a8a;
  --grey-btn:#4a4a4a;
  --page:#f2f2f2;
  --side:#e9e9e9;
  --foot:#ececec;
  --gold-border:#e0b64a;
  --dark-border:#4a4a4a;
  --white:#fff;
}
*{box-sizing:border-box;margin:0;padding:0}
html,body{width:1200px;height:2455px;overflow:hidden}
body{position:relative;background:var(--page);font-family:"Arimo",Arial,sans-serif;color:var(--ink)}
.abs{position:absolute}

/* header */
.site-header{position:absolute;left:0;top:0;width:1200px;height:183px;background:var(--white)}
.stripe{position:absolute;left:0;width:1200px;height:6px;display:flex}
.stripe span{flex:1}
.stripe .s1{background:var(--green)}.stripe .s2{background:var(--plum)}.stripe .s3{background:var(--yellow)}.stripe .s4{background:var(--orange)}.stripe .s5{background:var(--green-dark)}
.stripe.top{top:0;height:4px}
.stripe.bottom{top:176px;height:7px}
.brand{position:absolute;left:120px;top:30px;width:200px;height:130px}
.brand .mark{position:absolute;left:0;top:0;width:34px;height:34px;border-radius:50%;background:var(--green)}
.brand .name{position:absolute;left:44px;top:2px;font-size:26px;font-weight:700;color:var(--plum);line-height:30px;width:160px}
.brand .tag{position:absolute;left:44px;top:72px;font-size:15px;color:var(--green);font-weight:400}
.contact-row{position:absolute;left:396px;top:22px;display:flex;gap:34px;font-size:16px;align-items:center}
.contact-row .item{display:flex;align-items:center;gap:10px}
.social-top{position:absolute;left:848px;top:18px;display:flex;gap:14px}
.social-top span{width:36px;height:36px;border-radius:50%;display:block}
.main-nav{position:absolute;left:394px;top:99px;width:686px;height:50px;background:var(--white);box-shadow:0 3px 5px rgba(0,0,0,.25);display:flex;align-items:center;justify-content:space-around;font-size:25px}
.main-nav a{color:var(--ink);text-decoration:none}
.main-nav a.active{color:var(--green)}
.main-nav .sep{width:2px;height:22px;background:#333}

/* hero */
.hero{position:absolute;left:0;top:183px;width:1200px;height:496px;
  background:linear-gradient(90deg,#2c3f55 0%,#5d7290 18%,#b89b7a 35%,#d7b98c 48%,#8a5a3a 60%,#e2b21c 75%,#556f93 92%,#3e4a5a 100%)}
.hero-arrow{position:absolute;top:228px;width:45px;height:48px;background:var(--green-dark)}
.hero-arrow.prev{left:120px}.hero-arrow.next{left:1035px}
.hero-arrow svg{display:block;margin:12px auto}

/* sidebar column */
.side-col{position:absolute;left:764px;top:679px;width:436px;height:1536px;background:var(--side);box-shadow:inset 6px 0 8px -4px rgba(0,0,0,.12)}

/* about */
.about-title{position:absolute;left:200px;top:776px;width:320px;display:flex;align-items:center;justify-content:center;gap:8px;font-size:25px;letter-spacing:.5px}
.dot{width:9px;height:9px;border-radius:50%;display:inline-block}
.about-photo{position:absolute;left:118px;top:840px;width:225px;height:288px;border:3px solid #111;box-shadow:0 14px 14px -8px rgba(0,0,0,.45);
  background:linear-gradient(160deg,#d7c6c0,#b78a7a 45%,#e7d6cf)}
.about-text{position:absolute;left:363px;top:834px;width:318px;height:376px;overflow:hidden;font-size:19.5px;line-height:25px;color:var(--grey-text);text-align:justify;hyphens:auto}
.btn{display:inline-block;background:var(--grey-btn);color:var(--white);font-size:20px;text-align:center}
.read-more{position:absolute;left:560px;top:1246px;width:126px;height:36px;line-height:36px;border:1px solid #ccc}

/* feature cards */
.feature{position:absolute;left:120px;width:566px;height:230px;color:var(--white)}
.feature .photo{position:absolute;left:0;top:0;width:214px;height:230px;border:3px solid #111}
.feature h2{position:absolute;left:214px;top:18px;width:352px;text-align:center;font-size:30px;font-weight:400}
.feature p{position:absolute;left:236px;top:66px;width:312px;font-size:15.5px;line-height:29px;text-align:center;font-weight:700;height:116px;overflow:hidden}
.feature .btn{position:absolute;left:426px;top:192px;width:110px;height:30px;line-height:30px;font-size:17px}
.feature.list{top:1357px;background:var(--green)}
.feature.friends{top:1640px;background:var(--plum)}
.feature.aap{top:1925px;background:var(--orange)}

/* partners */
.partners{position:absolute;left:807px;top:766px;width:273px}
.partner{position:relative;height:112px;margin-bottom:4px;background:#f7f7f7;border:2px solid var(--gold-border)}
.partner.dark{border-color:var(--dark-border)}
.partner .badge{position:absolute;top:8px;width:128px;height:94px;border-radius:4px}
.partner .copy{position:absolute;top:10px;width:118px;font-size:15.5px;line-height:20px;color:#333}
.partner .more{position:absolute;bottom:4px;font-size:17px;color:var(--green)}
.partner.l .badge{left:8px}.partner.l .copy{left:148px}.partner.l .more{left:164px}
.partner.r .badge{right:8px}.partner.r .copy{left:14px}.partner.r .more{left:24px}

/* footer */
.site-footer{position:absolute;left:0;top:2215px;width:1200px;height:240px;background:var(--foot);box-shadow:0 -6px 10px rgba(0,0,0,.08)}
.site-footer h3{position:absolute;font-size:17px;font-weight:700;letter-spacing:.5px}
.divider{position:absolute;top:28px;width:1px;height:190px;background:#d6d6d6}
.map{position:absolute;left:137px;top:78px;width:137px;height:115px;border:1px solid #bbb;background:linear-gradient(135deg,#e4e4dc,#d3d8cc)}
.addr{position:absolute;left:295px;top:74px;font-size:17px;line-height:25px}
.links{position:absolute;left:607px;top:72px;list-style:none;font-size:15px;line-height:25px}
.social-foot{position:absolute;left:838px;top:93px;display:flex;gap:16px}
.social-foot span{width:36px;height:36px;border-radius:50%;background:#555;display:block}
.legal{position:absolute;left:951px;top:180px;font-size:10px;color:#444;line-height:20px}
</style>
</head>
<body>

<header class="site-header">
  <div class="stripe top"><span class="s1"></span><span class="s2"></span><span class="s3"></span><span class="s4"></span><span class="s5"></span></div>
  <div class="brand">
    <span class="mark"></span>
    <span class="name">Bright<br>Harbor</span>
    <span class="tag">We Nurture People</span>
  </div>
  <div class="contact-row">
    <span class="item">
      <svg width="38" height="22" viewBox="0 0 38 22"><path d="M3 8 Q19 -2 35 8 L32 12 L26 10 L26 7 Q19 4 12 7 L12 10 L6 12 Z" fill="#6aa512"/><rect x="9" y="12" width="20" height="9" rx="2" fill="#6aa512"/></svg>
      (555) 014-2270
    </span>
    <span class="item">
      <svg width="32" height="22" viewBox="0 0 32 22"><rect x="1" y="1" width="30" height="20" fill="none" stroke="#6aa512" stroke-width="2"/><path d="M1 1 L16 13 L31 1" fill="none" stroke="#6aa512" stroke-width="2"/></svg>
      hello@brightharbor.example
    </span>
  </div>
  <div class="social-top">
    <span style="background:#3b5998"></span>
    <span style="background:#29a9e1"></span>
    <span style="background:#6b4c3b"></span>
    <span style="background:#d23f31"></span>
    <span style="background:#2fb643"></span>
  </div>
  <nav class="main-nav">
    <a class="active" href="#">Home</a><span class="sep"></span>
    <a href="#">APP Listing</a><span class="sep"></span>
    <a href="#">KoruValer</a><span class="sep"></span>
    <a href="#">AAP</a><span class="sep"></span>
    <a href="#">Contact Us</a>
  </nav>
  <div class="stripe bottom"><span class="s1"></span><span class="s2"></span><span class="s3"></span><span class="s4"></span><span class="s5"></span></div>
</header>

<section class="hero" role="img" aria-label="Photo: a volunteer in denim hands a bag of bread to a smiling young woman in yellow at a community food drive">
  <span class="hero-arrow prev"><svg width="18" height="24" viewBox="0 0 18 24"><path d="M15 2 L4 12 L15 22" fill="none" stroke="#fff" stroke-width="4"/></svg></span>
  <span class="hero-arrow next"><svg width="18" height="24" viewBox="0 0 18 24"><path d="M3 2 L14 12 L3 22" fill="none" stroke="#fff" stroke-width="4"/></svg></span>
</section>

<aside class="side-col"></aside>

<main>
  <h1 class="about-title" style="font-weight:400">
    <span class="dot" style="background:#f5d3a8"></span><span class="dot" style="background:#f4c27a"></span><span class="dot" style="background:#7a5a6a"></span><span class="dot" style="background:#4f7f0c"></span>
    ABOUTS US
    <span class="dot" style="background:#4f7f0c"></span><span class="dot" style="background:#7a5a6a"></span><span class="dot" style="background:#f4c27a"></span><span class="dot" style="background:#f5d3a8"></span>
  </h1>
  <div class="about-photo" role="img" aria-label="Photo: many young people's hands stacked together in the middle of a circle"></div>
  <p class="about-text">Lorem Ipsum is simply dummy text of the printing and typesetting industry. Lorem Ipsum has been the industry's standard dummy text ever since the 1500s, when an unknown printer took a galley of type and scrambled it to make a type specimen book. It has survived not only five centuries, but also the leap into electronic typesetting, remaining essentially unchanged. It was popularised in the 1960s with the release of Letraset sheets containing Lorem Ipsum passages, and more recently with desktop</p>
  <a class="btn read-more">Read More</a>

  <article class="feature list">
    <div class="photo" role="img" aria-label="Photo: volunteers in green shirts packing donation boxes" style="background:linear-gradient(160deg,#c9b8a6,#3f8a5a 55%,#b89a70)"></div>
    <h2>AAP LIST</h2>
    <p>Lorem Ipsum is simply dummy text of the printing and typesetting industry. Lorem Ipsum has been the industry's standard dummy text ever since the 1500s, when</p>
    <a class="btn">Click Here</a>
  </article>

  <article class="feature friends">
    <div class="photo" role="img" aria-label="Photo: a group of young friends jumping on a grassy field" style="background:linear-gradient(180deg,#d9dde2 0%,#b9c2cc 45%,#7a6a5a 65%,#6b8f3a 100%)"></div>
    <h2>KoruValer</h2>
    <p>Lorem Ipsum is simply dummy text of the printing and typesetting industry. Lorem Ipsum has been the industry's standard dummy text ever since the 1500s, when</p>
    <a class="btn">Click Here</a>
  </article>

  <article class="feature aap">
    <div class="photo" role="img" aria-label="Photo: zebras standing on dry savanna grass" style="background:linear-gradient(180deg,#c7b27a 0%,#6a6a62 45%,#a8925a 100%)"></div>
    <h2>AAP</h2>
    <p>Lorem Ipsum is simply dummy text of the printing and typesetting industry. Lorem Ipsum has been the industry's standard dummy text ever since the 1500s, when</p>
    <a class="btn">Click Here</a>
  </article>

  <div class="partners">
    <div class="partner l"><span class="badge" style="background:#c8102e"></span><span class="copy">Lorem Ipsum is simply dum my textLorem</span><span class="more">Click Here</span></div>
    <div class="partner r dark"><span class="badge" style="background:#1d4f9c"></span><span class="copy">Lorem Ipsum is simply dum my textLorem</span><span class="more">Click Here</span></div>
    <div class="partner l"><span class="badge" style="background:#6a1b8a"></span><span class="copy">Lorem Ipsum is simply dum my textLorem</span><span class="more">Click Here</span></div>
    <div class="partner r"><span class="badge" style="background:#d0021b"></span><span class="copy">Lorem Ipsum is simply dum my textLorem</span><span class="more">Click Here</span></div>
    <div class="partner l"><span class="badge" style="background:#2e8b3a"></span><span class="copy">Lorem Ipsum is simply dum my textLorem</span><span class="more">Click Here</span></div>
    <div class="partner r dark"><span class="badge" style="background:#1a2f7a"></span><span class="copy">Lorem Ipsum is simply dum my textLorem</span><span class="more">Click Here</span></div>
    <div class="partner l dark"><span class="badge" style="background:#1d5fa8"></span><span class="copy">Lorem Ipsum is simply dum my textLorem</span><span class="more">Click Here</span></div>
    <div class="partner r"><span class="badge" style="background:#d4252a"></span><span class="copy">Lorem Ipsum is simply dum my textLorem</span><span class="more">Click Here</span></div>
    <div class="partner l"><span class="badge" style="background:#1c4fa0"></span><span class="copy">Lorem Ipsum is simply dum my textLorem</span><span class="more">Click Here</span></div>
    <div class="partner r dark"><span class="badge" style="background:#1a2f7a"></span><span class="copy">Lorem Ipsum is simply dum my textLorem</span><span class="more">Click Here</span></div>
    <div class="partner l"><span class="badge" style="background:#1d5fa8"></span><span class="copy">Lorem Ipsum is simply dum my textLorem</span><span class="more">Click Here</span></div>
    <div class="partner r"><span class="badge" style="background:#d4252a"></span><span class="copy">Lorem Ipsum is simply dum my textLorem</span><span class="more">Click Here</span></div>
  </div>
</main>

<footer class="site-footer">
  <h3 style="left:137px;top:50px">Address</h3>
  <div class="map" role="img" aria-label="Map showing the office location with a pin"></div>
  <p class="addr">Lorem Ipsum is simply<br>dummy text of the printing and<br>typesetting industry<br>Phone: (555) 014-2270<br>Email: hello@brightharbor.example</p>
  <span class="divider" style="left:566px"></span>
  <h3 style="left:607px;top:50px">Important Links</h3>
  <ul class="links">
    <li>Home</li><li>AAP List</li><li>KoruValer</li><li>AAP</li><li>Contact Us</li>
  </ul>
  <span class="divider" style="left:788px"></span>
  <h3 style="left:838px;top:50px">Fallow Us</h3>
  <div class="social-foot"><span></span><span></span><span></span><span></span><span></span></div>
  <p class="legal">Site Map &nbsp;|&nbsp; Privacy &nbsp;|&nbsp; Site Credits<br>© 2014 Bright Harbor</p>
</footer>

</body>
</html>
```